Vehicle Design for electrician business

We need a vehicle design made for an Morvane KTL Truck. We need the logo to be used and include the following information. We are after something clean and modern, can be simple or more extravagant. We dont know what we are after at the moment and are open to your designs.

website: www.pltw.com.au
Ph: 02 5184 3960

```html
<!DOCTYPE html>
<html lang="en">
<head>
<meta charset="utf-8">
<title>PL &amp; TW Electrics – Truck Side Wrap</title>
<link rel="stylesheet" href="https://fonts.googleapis.com/css2?family=Roboto+Condensed:ital,wght@0,700;0,800;1,700;1,800&family=Roboto:ital,wght@1,700;1,900&display=swap">
<style>
  :root {
    --navy: #003a8c;
    --red: #e10613;
    --panel: #eef0ee;
    --frame: #c9cccb;
    --page: #e8e8e8;
    --white: #ffffff;
  }
  * { margin: 0; padding: 0; box-sizing: border-box; }
  html, body { width: 1200px; height: 620px; overflow: hidden; background: var(--page); }
  .wrap-panel {
    position: absolute; left: 20px; top: 82px; width: 1161px; height: 456px;
    background: var(--panel); border: 3px solid var(--frame); overflow: hidden;
  }
  .wrap-shapes { position: absolute; inset: 0; width: 100%; height: 100%; }
  .brand-name {
    position: absolute; left: 58px; top: 22px; width: 520px; text-align: center;
    font-family: "Roboto Condensed", sans-serif; font-weight: 800; color: var(--red);
    line-height: 0.95; text-transform: uppercase;
  }
  .brand-name .brand-initials { display: block; font-size: 72px; letter-spacing: 2px; }
  .brand-name .brand-trade { display: block; font-size: 112px; letter-spacing: 1px; }
  .tagline {
    position: absolute; left: 80px; top: 243px; color: var(--white);
    font-family: "Roboto", sans-serif; font-style: italic; font-weight: 700; line-height: 1.05;
  }
  .tagline .tagline-region { display: block; font-size: 17px; }
  .tagline .tagline-main { display: block; font-size: 26px; }
  .on-call { position: absolute; left: 65px; top: 316px; display: flex; align-items: center; gap: 8px; }
  .on-call-icon { width: 48px; height: 48px; }
  .on-call-text { font-family: "Roboto", sans-serif; font-style: italic; font-weight: 700; color: var(--red); line-height: 1.1; }
  .on-call-text .on-call-label { display: block; font-size: 16px; }
  .on-call-text .on-call-hours { display: block; font-size: 28px; }
  .on-call-text small { font-size: 16px; }
  .on-call-text .divider { display: inline-block; width: 1px; height: 24px; background: var(--red); margin: 0 6px; vertical-align: -3px; }
  .phone { position: absolute; left: 66px; top: 384px; display: flex; align-items: center; gap: 10px; }
  .phone-icon { width: 48px; height: 48px; }
  .phone-number {
    font-family: "Roboto Condensed", sans-serif; font-style: italic; font-weight: 800;
    font-size: 60px; color: var(--navy); letter-spacing: -1px; line-height: 1;
  }
  .services-heading {
    position: absolute; left: 745px; top: 8px; width: 280px; text-align: center;
    font-family: "Roboto", sans-serif; font-style: italic; font-weight: 900; font-size: 30px; color: var(--white);
  }
  .service-list { position: absolute; left: 727px; top: 52px; list-style: none; width: 420px; }
  .service-item { position: relative; padding-left: 16px; height: 43.5px; color: var(--white); font-family: "Roboto", sans-serif; font-style: italic; font-weight: 700; }
  .service-item::before {
    content: ""; position: absolute; left: 0; top: 13px; width: 10px; height: 10px; border-radius: 50%; background: var(--red);
  }
  .service-title { display: block; font-size: 21px; line-height: 1.05; }
  .service-note { display: block; font-size: 9px; line-height: 1.3; }
  .website {
    position: absolute; left: 645px; top: 342px; font-family: "Roboto", sans-serif;
    font-style: italic; font-weight: 900; font-size: 44px; color: var(--red);
  }
  .social-marks { position: absolute; left: 1045px; top: 416px; display: flex; gap: 14px; }
  .social-marks span { width: 20px; height: 20px; border-radius: 50%; background: var(--white); }
</style>
</head>
<body>
<div class="wrap-panel">
  <svg class="wrap-shapes" viewBox="0 0 1350 530" preserveAspectRatio="none" aria-hidden="true">
    <polygon class="tagline-band" points="77,280 725,280 680,347 77,347" fill="#003a8c"/>
    <polygon class="services-strip" points="885,0 1350,0 1350,8 880,8" fill="#003a8c"/>
    <polygon class="services-block" points="850,50 1350,50 1350,392 655,392 775,230 710,228" fill="#003a8c"/>
    <polygon class="services-flag" points="870,8 1215,8 1185,50 845,50" fill="#e10613"/>
    <polygon class="footer-band" points="600,458 1350,458 1350,530 548,530" fill="#003a8c"/>
  </svg>

  <div class="brand-name">
    <span class="brand-initials">PL &amp; TW</span>
    <span class="brand-trade">Electrics</span>
  </div>

  <div class="tagline">
    <span class="tagline-region">The Riverina’s</span>
    <span class="tagline-main">Leading Electrical Contractors</span>
  </div>

  <div class="on-call">
    <svg class="on-call-icon" viewBox="0 0 48 48" aria-hidden="true">
      <circle cx="24" cy="24" r="22" fill="none" stroke="#e10613" stroke-width="2.5"/>
      <circle cx="24" cy="24" r="17" fill="#e10613"/>
      <path d="M15 26 v-3 a9 9 0 0 1 18 0 v3" fill="none" stroke="#fff" stroke-width="2"/>
      <rect x="13" y="24" width="4" height="7" rx="1.5" fill="#fff"/>
      <rect x="31" y="24" width="4" height="7" rx="1.5" fill="#fff"/>
      <path d="M33 31 q0 4 -6 4" fill="none" stroke="#fff" stroke-width="1.6"/>
    </svg>
    <div class="on-call-text">
      <span class="on-call-label">On Call Services Available</span>
      <span class="on-call-hours">24 Hours<small> a Day</small><span class="divider"></span>7 Days <small>a Week</small></span>
    </div>
  </div>

  <div class="phone">
    <svg class="phone-icon" viewBox="0 0 50 50" aria-hidden="true">
      <circle cx="25" cy="25" r="25" fill="#003a8c"/>
      <path d="M18 12 l5 7 -3 4 q3 6 8 9 l4 -3 7 5 -3 5 q-14 0 -22 -17 z" fill="#fff"/>
    </svg>
    <span class="phone-number">02 5184 3960</span>
  </div>

  <div class="services-heading">SERVICES</div>
  <ul class="service-list">
    <li class="service-item"><span class="service-title">Air Conditioning &amp; Refrigeration</span><span class="service-note">Industrial, Commercial and Residential Air Conditioning and<br>Refrigeration Services</span></li>
    <li class="service-item"><span class="service-title">Fire Protection Services</span><span class="service-note">The Riverina’s Specialist Fire Protection Contractors</span></li>
    <li class="service-item"><span class="service-title">Solar Solutions</span><span class="service-note">Renewable Energy Specialists in the Riverina</span></li>
    <li class="service-item"><span class="service-title">Multi Service Maintenance</span><span class="service-note">Reliable, Ongoing Support Packages with PL &amp; TW</span></li>
    <li class="service-item"><span class="service-title">Specialist Services</span><span class="service-note">More Than Your Regular Electrician in the Riverina</span></li>
    <li class="service-item"><span class="service-title">Labour Hire</span><span class="service-note">Quality electrical and mechanical labour hire services in the Riverina region</span></li>
  </ul>

  <div class="website">www.pltw.com.au</div>
  <div class="social-marks" aria-hidden="true"><span></span><span></span></div>
</div>
</body>
</html>
```